Business card for mobile auto detailing company
Brisk auto detailing - Business card
Business card for mobile auto detailing company - Automotive
Creative Brief
Simple
Brisk Auto Detailing
We are mobile (We come to you)
marcus@briskautodetailing.example
briskautodetailing.example
One side should have just the logo with the text underneath and maybe some car design element The other side should have all of the contact information and probably the logo on it too. It should have a classy look to it and be very simple. I also want to say what we specialize in "Hand Wash, Waxing, Paint correction & Interior deep cleaning & More" I'm not really sure exactly how I would like this to look (hence the contest), however just very simple and stylish.
Logo on the back with some design element.

```html
<!DOCTYPE html>
<html lang="en">
<head>
<meta charset="utf-8">
<title>Brisk Auto Detailing – Business Card</title>
<link rel="stylesheet" href="https://fonts.googleapis.com/css2?family=Roboto:wght@400;700&family=Lora:ital,wght@1,500&display=swap">
<style>
  :root {
    --backdrop: #c9ccad;
    --card-black: #0f0f10;
    --card-white: #ffffff;
    --accent-cyan: #1cb9e6;
    --text-light: #f2f2f2;
    --text-muted: #bdbdbd;
    --text-dark: #1a2a3a;
  }
  * { margin: 0; padding: 0; box-sizing: border-box; }
  html, body {
    width: 1200px; height: 901px; overflow: hidden;
    background: var(--backdrop);
    font-family: "Roboto", Arial, sans-serif;
  }
  .card {
    position: absolute; width: 700px; height: 400px;
    box-shadow: 0 6px 18px rgba(0,0,0,0.25);
    overflow: hidden;
  }
  /* Logo side */
  .card-front { left: 430px; top: 40px; background: var(--card-black); }
  .front-brand {
    position: absolute; left: 0; right: 0; top: 150px; text-align: center;
  }
  .brand-name {
    font-weight: 700; font-size: 40px; color: var(--text-light);
    letter-spacing: 1px; text-transform: uppercase;
  }
  .brand-tagline {
    margin-top: 8px; font-size: 18px; letter-spacing: 3px;
    color: var(--accent-cyan);
  }
  /* Contact side */
  .card-back { left: 70px; top: 470px; background: var(--card-white); }
  .card-back svg.back-shapes { position: absolute; inset: 0; }
  .back-brand { position: absolute; left: 30px; top: 190px; width: 270px; }
  .back-brand .brand-name { font-size: 25px; color: var(--accent-cyan); letter-spacing: 0.5px; }
  .back-brand .brand-tagline { font-size: 15px; letter-spacing: 2px; margin-top: 4px; }
  .person { position: absolute; right: 60px; top: 40px; text-align: left; width: 260px; }
  .person-name { font-size: 25px; color: var(--text-light); }
  .person-role { font-size: 14px; color: var(--text-muted); margin-top: 2px; }
  .find-us {
    position: absolute; right: 48px; top: 118px;
    background: var(--accent-cyan); color: var(--card-black);
    font-size: 12px; padding: 2px 8px;
  }
  .contact-list {
    position: absolute; right: 32px; top: 175px; list-style: none;
    text-align: right;
  }
  .contact-list li {
    font-size: 14px; color: var(--text-light); line-height: 24px;
    display: flex; justify-content: flex-end; align-items: center; gap: 10px;
  }
  .contact-list svg { width: 14px; height: 14px; flex: none; }
  .specialties {
    position: absolute; left: 0; right: 0; top: 352px; height: 32px;
    text-align: center; line-height: 32px;
    font-family: "Lora", Georgia, serif; font-style: italic; font-size: 15px;
    color: var(--text-dark);
  }
</style>
</head>
<body>

<section class="card card-front" aria-label="Business card, logo side">
  <div class="front-brand">
    <div class="brand-name">Brisk Auto Detailing</div>
    <div class="brand-tagline">We are mobile</div>
  </div>
</section>

<section class="card card-back" aria-label="Business card, contact side">
  <svg class="back-shapes" width="700" height="400" viewBox="0 0 700 400" aria-hidden="true">
    <path d="M340 0 H700 V350 H300 C370 270 385 110 340 0 Z" fill="var(--card-black)"/>
    <rect x="0" y="350" width="700" height="36" fill="var(--accent-cyan)"/>
  </svg>

  <div class="back-brand">
    <div class="brand-name">Brisk Auto Detailing</div>
    <div class="brand-tagline">We are mobile</div>
  </div>

  <div class="person">
    <div class="person-name">Marcus Hale</div>
    <div class="person-role">Managing Director</div>
  </div>
  <div class="find-us">Find us on</div>

  <ul class="contact-list">
    <li>+11 555 010 247
      <svg viewBox="0 0 14 14"><path d="M3 1 L5.5 1 L6.5 4 L5 5.5 C6 7.5 7 8.5 8.5 9 L10 7.5 L13 8.5 L13 11 C13 12 12 13 11 13 C5.5 12.5 1.5 8.5 1 3 C1 2 2 1 3 1 Z" fill="var(--accent-cyan)"/></svg>
    </li>
    <li>marcus@briskautodetailing.example
      <svg viewBox="0 0 14 14"><rect x="1" y="3" width="12" height="8" fill="var(--accent-cyan)"/><path d="M1 3 L7 8 L13 3" stroke="var(--card-black)" fill="none"/></svg>
    </li>
    <li>briskautodetailing.example
      <svg viewBox="0 0 14 14"><circle cx="7" cy="7" r="5.5" fill="none" stroke="var(--accent-cyan)" stroke-width="1.5"/><path d="M1.5 7 H12.5 M7 1.5 V12.5" stroke="var(--accent-cyan)"/></svg>
    </li>
    <li>briskautodetailing
      <svg viewBox="0 0 14 14"><rect x="1" y="1" width="12" height="12" fill="var(--accent-cyan)"/></svg>
    </li>
    <li>@briskautodetailing
      <svg viewBox="0 0 14 14"><circle cx="7" cy="7" r="6" fill="var(--accent-cyan)"/></svg>
    </li>
  </ul>

  <div class="specialties">"Hand Wash, Waxing, Paint correction &amp; Interior deep cleaning &amp; More"</div>
</section>

</body>
</html>
```